Contest - label design for a health related product with 4 color variations

Nuvera-Store (http://www.nuvera-store.example) is an online shop selling health related products and nutritional supplements, such as algae products, wheat grass and barley grass powder. These products have a positive impact on a person's health. Through Craft Hive, we have designed already a logo for the shop and now we need to create labels that will be placed on a brown glass bottle (see attachment). The logo shall be used without the slogan 'One life. Live it healthy.' when creating the label.

Your job is to design a label with 4 color variations, blue, green, red and yellow. The measurements of the label is 80 mm x 173 mm, but please add 3 mm bleed to each side.

The information that has to go on the label can be taken from the attachment 'label information.pdf'. For the sake of communication, we will divide the label into 3 parts

- left
- middle
- right

The left part and the right part are fixed as this contains legal information. Please use easy to read fonts, non-serifed fonts, such as Arial, Verdana, Calibri. The left part contains a table and if Illustrator provides the possibility for tables, please use it as we need to be able to easily add and remove rows of the table.

The middle part contains the product description, the product quantity (i.e. 100 g), our logo without the slogan 'One live. Live it healthy.' and logos indicating the organic quality of the product (please see attachments). For the product name (i.e. KEM-Tangen) and the quantity (i.e. 100 Tabletten, 200 g) use the attached Lato font. Please note that the vertical position of our logo, the product name and the organic logos has NOT been set yet. You are free to position them where ever you feel in the middle part of the label.

Target Market(s)

Health concious people between 25 and 70

Industry/Entity Type

Health

Requirements
Must have
• - the attached logo without the slogan "One life...."
- the following attributes: healthy, joyful, vivid, lively, abstract, minimalistic
- colors that go along with our logo and the website www.nuvera-store.example
- all fonts need to be editable and not rendered
- the left part should have an editable table where we can add rows if necessary
- the attached font for product name and quantity
- 3 mm bleed on each side, so the final design is 6 mm wider and higher
- the final design will be in editable Illustrator files of a recent version.
Should not have
• - many overlaying, confusing lines or layers
- dark colors
- heavy appearance

```html
<!DOCTYPE html>
<html lang="de">
<head>
<meta charset="utf-8">
<title>KEM-Tangen Etikett</title>
<link rel="stylesheet" href="https://fonts.googleapis.com/css2?family=Lato:wght@300;400&family=Open+Sans:wght@400;700&display=swap">
<style>
  :root {
    --canvas: #ffffff;
    --edge: #c9d3e6;
    --navy: #373f73;
    --panel-top: #2e5b95;
    --panel-bottom: #0cb2ea;
    --hero-top: #12aeea;
    --hero-bottom: #2c5c9e;
    --text-light: #ffffff;
    --brand-grey: #6b6b6b;
    --brand-orange: #f2a51c;
    --badge-green: #7cb342;
    --badge-grey: #9a9a9a;
  }
  * { margin: 0; padding: 0; box-sizing: border-box; }
  html, body { width: 1200px; height: 568px; overflow: hidden; background: var(--canvas); }
  .label {
    position: relative; width: 1200px; height: 568px;
    background: var(--canvas); border: 1px solid var(--edge);
    font-family: "Open Sans", Arial, sans-serif; color: var(--text-light);
  }
  .top-band { position: absolute; left: 12px; top: 12px; width: 1176px; height: 48px; background: var(--navy); }
  .side-panel {
    position: absolute; top: 60px; width: 294px; height: 497px;
    background: linear-gradient(180deg, var(--panel-top) 0%, #1f7fc0 50%, var(--panel-bottom) 100%);
    padding: 44px 18px 0 16px; font-size: 12.5px; line-height: 17.5px;
  }
  .side-panel--left { left: 12px; }
  .side-panel--right { left: 894px; }
  .info-block { margin-bottom: 17.5px; }
  .info-block h3 { font-weight: 700; font-size: 12.5px; }
  .hint-list { list-style: none; }
  .hint-list li { padding-left: 10px; text-indent: -10px; }
  .hero {
    position: absolute; left: 306px; top: 60px; width: 588px; height: 370px;
    background: linear-gradient(180deg, var(--hero-top) 0%, #1b8fd3 55%, var(--hero-bottom) 100%);
    text-align: center; font-family: "Lato", Arial, sans-serif;
  }
  .product-name { position: absolute; left: 0; right: 0; top: 238px; font-size: 52px; font-weight: 400; line-height: 60px; }
  .product-quantity { position: absolute; left: 0; right: 0; top: 313px; font-size: 20px; font-weight: 300; }
  .brand-strip { position: absolute; left: 306px; top: 430px; width: 588px; height: 127px; background: var(--canvas); }
  .brand-mark { position: absolute; left: 34px; top: 18px; }
  .brand-name { position: absolute; left: 181px; top: 83px; font-size: 19px; color: var(--brand-grey); }
  .organic-badges { position: absolute; left: 434px; top: 36px; }
</style>
</head>
<body>
<div class="label">
  <div class="top-band"></div>

  <section class="side-panel side-panel--left">
    <div class="info-block">
      <h3>Zutaten</h3>
      <p>KEM-Tangen (AFA-Aphanizonenon Flos Aqua)<br>aus dem Klamath Lake, bei 37° Celsius<br>getrocknet.</p>
    </div>
    <div class="info-block">
      <h3>Nährwertangaben in 100 g pro Kapsel</h3>
      <p>Kohlenhydrate<br>Fett<br>Eiweiß<br>Brennwert (kJ / kcal)</p>
    </div>
    <div class="info-block">
      <h3>Inhaltsstoffe</h3>
      <p>Vitamin C (<strong>pro Kapsel</strong> 50,2 mg), (<strong>%RDA</strong> 50 %)</p>
    </div>
    <div class="info-block">
      <h3>Vertrieb</h3>
      <p>Merrow Field Limited<br>Lindenhofgasse 12<br>1140 Wien<br>Österreich</p>
    </div>
  </section>

  <section class="hero">
    <h1 class="product-name">KEM-Tangen</h1>
    <p class="product-quantity">100 Tabletten, 200 g</p>
  </section>

  <section class="brand-strip">
    <svg class="brand-mark" width="140" height="80" viewBox="0 0 140 80" aria-hidden="true">
      <circle cx="70" cy="40" r="30" fill="var(--brand-orange)"/>
    </svg>
    <span class="brand-name">Nuvera-Store</span>
    <svg class="organic-badges" width="140" height="50" viewBox="0 0 140 50" aria-hidden="true">
      <polygon points="14,2 44,2 56,25 44,48 14,48 2,25" fill="none" stroke="var(--badge-grey)" stroke-width="2.5"/>
      <rect x="70" y="2" width="68" height="46" fill="var(--badge-green)"/>
    </svg>
  </section>

  <section class="side-panel side-panel--right">
    <div class="info-block">
      <h3>Verzehrempfehlung</h3>
      <p>3 x täglich 3 – 5 Tabletten unzerkaut mit<br>Wasser zu den Mahlzeiten einnehmen.</p>
    </div>
    <div class="info-block">
      <h3>Hinweise</h3>
      <ul class="hint-list">
        <li>- Die angegebene tägliche Verzehrmenge<br>sollte nicht überschritten werden.</li>
        <li>- Nahrungsergänzungsmittel sind kein Ersatz<br>für eine ausgewogene und<br>abwechslungsreiche Ernährung.</li>
        <li>- Das Produkt lichtgeschützt, verschlossen<br>und außerhalb der Reichweite von kleinen<br>Kindern aufbewahren.</li>
        <li>- Während der Schwangerschaft und<br>Stillzeiten sollte vor dem Verzehr von<br>Nahrungsergänzungsmitteln ein Arzt<br>konsultiert werden.</li>
      </ul>
    </div>
    <div class="info-block">
      <h3>Mindesthaltbarkeitsdatum</h3>
      <p>Siehe Boden.</p>
    </div>
  </section>
</div>
</body>
</html>
```